Modern, Clean website for painting service.

We are working with a company called Brush Harbor and building a new website for them.

Some sites to use for content/competitors and inspiration:

https://www.coatwellcrew.example
https://ridgeline-coats.example
https://tevinhallorpainting.example

Thank you for taking the time to consider designing a website for us. We are web developers based in Stockton, CA, USA. Most of our projects go through the same process. Understanding this process may help you win a project with us. We custom-code all of our websites in-house. We don’t have any requirements as to what tools you use for your design, but we prefer Figma files. For any design that we label as four-stars, we send it to the client for review. The client picks the final design they want us to use. Once we complete this process, we will continue to show additional clients all the four-star sites and purchase them later. Your designs will have multiple chances to sell. For better chances of success, we ask that you follow these guidelines.

IMAGES:
If you use any images or icons in the design, we ask that you have a link to the asset so we can purchase the image/icon. Most of the designs we submit do not have the customer’s images on them unless they have some great images. Be creative; show us the feeling you are trying to portray with your image choices. Use any royalty-free site you choose. We subscribe to Adobe and mainly use their images, but we can purchase images outside of Adobe. PLEASE NOTE: we will not submit designs to clients with watermarks on the images.

FONTS:
We ask that you identify the fonts used in the design. This can be done in a message if you want. We typically use Google Fonts and Adobe Fonts.

CONTENT:
We're always open to different content and ideas. We often submit designs with stock images so the client can see our vision. We typically take pictures after the website launch to use their images with our vision. Lorem Ipsum is fine for paragraphs, but we ask that you write the headers in correct English. We want to be able to show the vision and identify the sections of the website.

INSPIRATION:
We typically add a couple of links in the brief of websites we like to help you get started in your design.

REVISIONS:
We do not often ask for revisions of the designs unless we see something in the design that may not appeal to the client. If there are slight changes that we want to make, we do that in the development process.

FEEDBACK:
We rarely give feedback on designs during the design process. We are working on many website projects and do not have the time to provide feedback. We usually respond if your request is well thought out and asks specific questions, but a note asking “feedback, please” usually goes unanswered.

```html
<!DOCTYPE html>
<html lang="en">
<head>
<meta charset="utf-8">
<title>Brush Harbor — Precision Painting</title>
<link rel="stylesheet" href="https://fonts.googleapis.com/css2?family=Open+Sans:wght@400;600;700;800&family=Lato:wght@400;700&display=swap">
<style>
:root{
  --navy:#0c2344;
  --blue:#1a4585;
  --red:#a3001e;
  --ink:#333a45;
  --muted:#5b616b;
  --light:#f6f6f7;
  --dark:#1f2329;
  --white:#fff;
}
*{margin:0;padding:0;box-sizing:border-box}
html,body{width:1200px;height:4703px;overflow:hidden}
body{font-family:"Lato",sans-serif;color:var(--ink);background:var(--white)}
h1,h2,h3,h4{font-family:"Open Sans",sans-serif}
.section{position:relative;width:1200px}
.abs{position:absolute}
.btn{position:absolute;display:flex;align-items:center;justify-content:center;background:var(--red);color:var(--white);font:700 11px "Open Sans",sans-serif;letter-spacing:.3px;text-transform:uppercase;border-radius:3px}
.section-title{position:absolute;left:0;width:1200px;text-align:center;color:var(--blue);font-size:30px;font-weight:700;letter-spacing:.3px}
.section-lead{position:absolute;left:330px;width:540px;text-align:center;font-size:13px;line-height:22px;color:var(--muted)}
.photo{position:absolute}

/* header */
.header{height:80px;background:var(--white);box-shadow:0 1px 4px rgba(0,0,0,.08);z-index:2}
.brand{position:absolute;left:158px;top:20px;display:flex;align-items:center;gap:8px;font:700 14px "Open Sans",sans-serif;color:var(--navy)}
.brand i{display:block;width:14px;height:14px;background:var(--red)}
.topbar{position:absolute;left:405px;top:0;right:0;height:26px;background:var(--white);font:600 9px "Open Sans",sans-serif;color:var(--navy)}
.topbar .curve{position:absolute;left:-40px;top:0}
.topbar .addr{position:absolute;left:48px;top:8px;display:flex;gap:6px;align-items:center}
.topbar .follow{position:absolute;left:300px;top:8px;display:flex;gap:5px;align-items:center}
.topbar .follow span.dot{width:7px;height:7px;border-radius:50%;background:var(--navy)}
.topbar .quote{position:absolute;left:435px;top:0;width:111px;height:24px;border-radius:0;font-size:9px}
.nav{position:absolute;top:50px;left:0;font:600 11px "Open Sans",sans-serif;color:#6a707a}
.nav a{position:absolute;white-space:nowrap;color:inherit;text-decoration:none}
.nav a.active{color:var(--blue)}

/* hero */
.hero{height:683px;overflow:hidden}
.hero .photo{inset:0;background:linear-gradient(100deg,#3d4349 0%,#5c6468 45%,#707a7c 70%,#58605f 100%)}
.hero .welcome{left:111px;top:196px;color:#e8e8e8;font-size:12px;display:flex;align-items:center;gap:14px}
.hero .welcome span{width:46px;height:1px;background:#e8e8e8}
.hero h1{left:111px;top:218px;width:420px;color:var(--white);font-size:42px;line-height:58px;font-weight:600}
.hero p{left:111px;top:352px;width:405px;color:#eee;font-size:13px;line-height:21px}
.hero .btn{left:111px;top:460px;width:192px;height:40px;text-transform:none;font-size:12px}

/* why */
.why{height:559px;background:var(--white)}
.why .section-title{top:80px}
.why .section-lead{top:128px;left:330px}
.card{position:absolute;top:207px;width:231px;height:215px;background:var(--white);box-shadow:0 2px 14px rgba(0,0,0,.09);text-align:center}
.card svg{margin-top:30px}
.card h3{margin-top:12px;color:var(--blue);font-size:18px;line-height:25px;font-weight:600}
.card p{margin:16px auto 0;width:185px;font-size:13px;line-height:22px;color:var(--muted)}
.card.featured{background:var(--navy)}
.card.featured h3,.card.featured p{color:var(--white)}
.why .btn{left:521px;top:462px;width:172px;height:39px}

/* smart */
.smart{height:510px}
.smart .panel{position:absolute;left:281px;top:0;right:0;height:466px;background:var(--navy)}
.smart .photo{left:0;top:62px;width:581px;height:448px;background:linear-gradient(120deg,#d7dbe0,#b4bcc6 50%,#8a9299);z-index:1}
.smart h2{left:632px;top:92px;color:var(--white);font-size:30px;font-weight:600}
.smart p{left:632px;width:445px;color:#dfe4ec;font-size:13px;line-height:22px}
.smart .btn{left:632px;top:329px;width:171px;height:40px}

/* services */
.services{height:679px;background:var(--light)}
.services .section-title{top:78px}
.services .section-lead{top:134px}
.service{position:absolute;top:231px;width:322px;height:380px}
.service .photo{left:0;top:0;width:322px;height:234px}
.service .box{position:absolute;left:20px;top:176px;width:282px;height:201px;background:var(--white);box-shadow:0 2px 14px rgba(0,0,0,.08);padding:24px 22px 0 43px}
.service h3{color:var(--blue);font-size:20px;font-weight:400;margin-left:-2px}
.service p{margin-top:8px;font-size:13px;line-height:22px;color:var(--muted)}
.service a{display:block;margin-top:10px;font:700 10px "Open Sans",sans-serif;color:var(--red);text-decoration:none}
.service.featured .box{background:var(--navy)}
.service.featured h3,.service.featured p,.service.featured a{color:var(--white)}

/* cta */
.cta{height:297px;overflow:hidden}
.cta .photo{inset:0;background:linear-gradient(90deg,#1e2f4a,#34476a 40%,#2a3c5c 70%,#1b2a44)}
.cta .phone{left:0;width:1200px;top:50px;display:flex;justify-content:center;align-items:center;gap:12px;color:var(--white);font:600 22px "Open Sans",sans-serif}
.cta h2{left:0;width:1200px;top:94px;text-align:center;color:var(--white);font-size:30px;font-weight:600}
.cta p{left:370px;width:460px;top:150px;text-align:center;color:#e4e8ef;font-size:13px;line-height:22px}
.cta .outline{position:absolute;left:517px;top:211px;width:173px;height:40px;border:1px solid var(--white);border-radius:3px;color:var(--white);font:700 10px "Open Sans",sans-serif;display:flex;align-items:center;justify-content:center}

/* projects */
.projects{height:640px;background:var(--white)}
.projects .section-title{top:80px}
.projects .section-lead{top:140px}
.proj-side{position:absolute;top:218px;height:352px;width:223px}
.proj-left{left:124px;background:linear-gradient(160deg,#4c6a3a,#2c3c52 55%,#1f2c44);clip-path:polygon(0 17%,100% 0,100% 100%,0 72%)}
.proj-right{left:856px;background:linear-gradient(200deg,#c9b39b,#5d6f8a 50%,#2b3e5c);clip-path:polygon(0 0,100% 17%,100% 72%,0 100%)}
.proj-main{position:absolute;left:365px;top:218px;width:477px;height:352px;background:radial-gradient(circle at 50% 45%,#f2b97a 0,#a0552e 18%,#3a3242 45%,#12203a 80%)}
.proj-main h4{position:absolute;left:33px;top:226px;color:var(--white);font-size:17px;font-weight:600}
.proj-main .date{position:absolute;left:33px;top:254px;color:var(--white);font:700 9px "Open Sans",sans-serif}
.proj-main p{position:absolute;left:33px;top:272px;width:390px;color:#e8e8e8;font-size:10px;line-height:15px}

/* contact */
.contact{height:807px;background:var(--light)}
.contact .section-title{top:66px}
.contact .section-lead{top:124px}
.contact-box{position:absolute;left:91px;top:209px;width:1014px;height:459px;background:var(--white)}
.contact-info{position:absolute;left:0;top:0;width:510px;height:459px;background:linear-gradient(120deg,#2c4460 0%,#3b5068 50%,#2e4158);color:var(--white)}
.contact-info .in{position:absolute;left:86px;top:68px}
.contact-info h4{font-size:15px;font-weight:600}
.contact-info .call{margin-top:20px;font:400 21px "Open Sans",sans-serif}
.contact-info .mail{font-size:11px;margin-top:4px}
.contact-info .blk{margin-top:26px;font-size:12px;line-height:18px}
.contact-info .blk b{font-size:11px}
.socials{display:flex;gap:10px;margin-top:34px}
.socials span{width:30px;height:30px;border-radius:50%;background:rgba(255,255,255,.28)}
.socials span.on{background:var(--white)}
.form{position:absolute;left:595px;top:0}
.form h4{position:absolute;top:58px;left:0;white-space:nowrap;color:var(--blue);font-size:16px;font-weight:700}
.field{position:absolute;left:0;width:334px;height:33px;background:#f1f2f4;font-size:10px;color:#8a8f96;padding:10px 14px}
.form .btn{left:0;top:369px;width:111px;height:36px}

/* footer */
.footer{height:448px;background:var(--dark);color:#d8dbe0}
.infobar{position:absolute;left:66px;top:-55px;width:1068px;height:104px;background:var(--red);border-radius:8px;color:var(--white)}
.info{position:absolute;top:28px;display:flex;gap:16px;align-items:flex-start}
.info h4{font-size:18px;font-weight:600}
.info p{font-size:13px;margin-top:6px;white-space:nowrap}
.fcol{position:absolute;top:133px}
.fcol h4{color:var(--white);font-size:18px;font-weight:600}
.fcol .rule{width:34px;height:2px;background:#b08a6a;margin:16px 0 22px}
.fcol p{font-size:13px;line-height:31px;width:310px}
.fcol .more{color:#c58a64;font-size:15px;text-decoration:underline}
.links{display:grid;grid-template-columns:177px 150px;row-gap:14px;font-size:13px}
.links a{color:#d8dbe0;text-decoration:underline}
.sub{display:flex;width:338px;height:54px}
.sub div{flex:1;background:var(--white);color:var(--ink);font-size:12px;padding:20px 16px}
.sub span{width:64px;background:var(--red);display:flex;align-items:center;justify-content:center}
.fbottom{position:absolute;left:0;top:383px;width:1200px;height:65px;border-top:1px solid #3a3f46}
.fbrand{position:absolute;left:66px;top:0;width:171px;height:65px;background:var(--red);display:flex;align-items:center;justify-content:center;gap:8px;color:var(--white);font:700 13px "Open Sans",sans-serif}
.fbrand i{width:12px;height:12px;background:var(--white)}
.fsocial{position:absolute;left:902px;top:0;display:flex}
.fsocial span{width:58px;height:65px;border-left:1px solid #3a3f46;display:flex;align-items:center;justify-content:center}
.fsocial span i{width:12px;height:12px;border-radius:50%;background:#5a6068}
</style>
</head>
<body>

<header class="section header">
  <div class="brand"><i></i>Brush Harbor</div>
  <div class="topbar">
    <svg class="curve" width="60" height="26" viewBox="0 0 60 26"><path d="M0 0 C20 0 30 26 60 26" fill="none" stroke="#d9dce1" stroke-width="1"/></svg>
    <div class="addr">
      <svg width="8" height="10" viewBox="0 0 8 10"><path d="M4 0a3.5 3.5 0 0 0-3.5 3.5C.5 6 4 10 4 10s3.5-4 3.5-6.5A3.5 3.5 0 0 0 4 0z" fill="#0c2344"/></svg>
      48 Easel Lane, Stockton, CA 95202
    </div>
    <div class="follow">Follow Us: <span class="dot"></span><span class="dot"></span><span class="dot"></span></div>
    <div class="btn quote">GET QUOTATION</div>
  </div>
  <nav class="nav">
    <a class="active" style="left:391px">Home</a>
    <a style="left:483px">About Us</a>
    <a style="left:576px">Services</a>
    <a style="left:670px">Gallery</a>
    <a style="left:758px">Our Team</a>
    <a style="left:863px">Contact Us</a>
  </nav>
</header>

<section class="section hero">
  <div class="photo" role="img" aria-label="Smiling painter holding a paint roller beside a ladder"></div>
  <div class="abs welcome">Welcome <span></span></div>
  <h1 class="abs">Precision painting for perfectionists</h1>
  <p class="abs">Lorem ipsum dolor sit amet, consectetur adipiscing elit, sed do eiusmod tempor incididunt ut labore et dolore magna Lorem ipsum dolor sit amet, consectetur adipiscing elit, sed do eiusmod tempor incididunt ut labore et dolore magna</p>
  <div class="btn">Discover more</div>
</section>

<section class="section why">
  <h2 class="section-title">Why We AreThe Best</h2>
  <p class="section-lead">Lorem ipsum dolor sit amet, consectetur adipiscing elit, sed do eiusmod tempor incididunt ut labore et dolore magna aliqua. Ut enim ad min</p>
  <div class="card" style="left:93px">
    <svg width="40" height="40" viewBox="0 0 40 40" fill="none" stroke="#a3001e" stroke-width="2"><circle cx="20" cy="20" r="6"/><path d="M20 4l4 4h6v6l4 6-4 6v6h-6l-4 4-4-4h-6v-6l-4-6 4-6V8h6z"/></svg>
    <h3>Expertise</h3>
    <p>Lorem ipsum dolor sit amet, consectetur adipiscing</p>
  </div>
  <div class="card featured" style="left:352px">
    <svg width="40" height="40" viewBox="0 0 40 40" fill="none" stroke="#fff" stroke-width="2"><circle cx="18" cy="18" r="12"/><circle cx="26" cy="26" r="6"/><circle cx="26" cy="26" r="2"/></svg>
    <h3>Comprehensive<br>Services</h3>
    <p>Lorem ipsum dolor sit amet, consectetur adipiscing</p>
  </div>
  <div class="card" style="left:612px">
    <svg width="40" height="40" viewBox="0 0 40 40" fill="none" stroke="#a3001e" stroke-width="2"><circle cx="20" cy="13" r="7"/><path d="M6 36c0-8 6-13 14-13s14 5 14 13z"/></svg>
    <h3>Experienced</h3>
    <p>Lorem ipsum dolor sit amet, consectetur adipiscing</p>
  </div>
  <div class="card" style="left:873px">
    <svg width="40" height="40" viewBox="0 0 40 40" fill="none" stroke="#a3001e" stroke-width="2"><path d="M20 4l5 10 11 2-8 8 2 11-10-5-10 5 2-11-8-8 11-2z"/></svg>
    <h3>Quality<br>Assurance</h3>
    <p>Lorem ipsum dolor sit amet, consectetur adipiscing</p>
  </div>
  <div class="btn">Learn more about</div>
</section>

<section class="section smart">
  <div class="panel"></div>
  <div class="photo" role="img" aria-label="Worker in a hard hat and safety vest painting a white exterior wall"></div>
  <h2 class="abs">Smart Solutions for Painting</h2>
  <p class="abs" style="top:142px">Lorem ipsum dolor sit amet, consectetur adipiscing elit, sed do eiusmod tempor incididunt ut labore et dolore magna aliqua. Ut enim ad minim veniam, quis nostrud ex</p>
  <p class="abs" style="top:214px">Lorem ipsum dolor sit amet, consectetur adipiscing elit, sed do eiusmod tempor incididunt ut labore et dolore magna aliqua. Ut enim ad minim veniam, quis nostrud exercitation ullamco laboris nisi ut aliquip ex ea commodo consequat. Duis aute iru</p>
  <div class="btn">Learn more about</div>
</section>

<section class="section services" style="margin-top:-44px">
  <h2 class="section-title" style="top:122px">What We Do</h2>
  <p class="section-lead" style="top:178px">Lorem ipsum dolor sit amet, consectetur adipiscing elit, sed do eiusmod tempor incididunt ut labore et dolore magna aliqua. Ut enim ad min</p>
  <div class="service" style="left:93px;top:275px">
    <div class="photo" role="img" aria-label="Painter in a cap sanding a window frame" style="background:linear-gradient(135deg,#e7e2d8,#a9a194 60%,#6e6a62)"></div>
    <div class="box"><h3>Residential Painting</h3><p>Lorem ipsum dolor sit amet, consectetur adipiscing elit, sed do eiusmod tempor incididunt ut labore et dolore magna aliqua.</p><a>LEARN MORE</a></div>
  </div>
  <div class="service featured" style="left:438px;top:275px">
    <div class="photo" role="img" aria-label="Painter on a ladder painting a commercial building facade" style="background:linear-gradient(180deg,#d8d4cc,#8f9a86 50%,#6b5e58)"></div>
    <div class="box"><h3>Commercial Painting</h3><p>Lorem ipsum dolor sit amet, consectetur adipiscing elit, sed do eiusmod tempor incididunt ut labore et dolore magna aliqua.</p><a>LEARN MORE</a></div>
  </div>
  <div class="service" style="left:785px;top:275px">
    <div class="photo" role="img" aria-label="Painter working in a bright room with a wooden ceiling" style="background:linear-gradient(180deg,#9b5a38,#e6ddd3 40%,#f2ece6)"></div>
    <div class="box"><h3>Specialized Coating</h3><p>Lorem ipsum dolor sit amet, consectetur adipiscing elit, sed do eiusmod tempor incididunt ut labore et dolore magna aliqua.</p><a>LEARN MORE</a></div>
  </div>
</section>

<section class="section cta" style="margin-top:44px">
  <div class="photo" role="img" aria-label="Modern glass office building at dusk"></div>
  <div class="abs phone">
    <svg width="34" height="34" viewBox="0 0 24 24" fill="none" stroke="#fff" stroke-width="1.3"><path d="M5 2h4l2 5-3 2a11 11 0 0 0 7 7l2-3 5 2v4a2 2 0 0 1-2 2A19 19 0 0 1 3 4a2 2 0 0 1 2-2z"/></svg>
    209-555-0147
  </div>
  <h2 class="abs">Experience the difference of true craftsmanship</h2>
  <p class="abs">Lorem ipsum dolor sit amet, consectetur adipiscing elit, sed do eiusmod tempor incididunt ut labore et dolore magna aliqua.</p>
  <div class="outline">CONTACT US NOW</div>
</section>

<section class="section projects">
  <h2 class="section-title">Our Recent Projects</h2>
  <p class="section-lead">Lorem ipsum dolor sit amet, consectetur adipiscing elit, sed do eiusmod tempor incididunt ut labore et dolore magna aliqua. Ut enim ad min</p>
  <div class="proj-side proj-left" role="img" aria-label="Workers installing solar panels on a roof"></div>
  <div class="proj-main" role="img" aria-label="Solar panels at sunset">
    <h4>Lorem Ipsum dolor sit amet</h4>
    <div class="date">08.08.2024</div>
    <p>Veniam culpa laborum enim laborum aliquaconsequat irure ea mollit minim cupidat Veniam culpa laborum enim laborum aliquaconsequat irure ea mollit minim cupidat</p>
  </div>
  <div class="proj-side proj-right" role="img" aria-label="Solar panels on a tiled roof"></div>
</section>

<section class="section contact">
  <h2 class="section-title">Contact Us</h2>
  <p class="section-lead">Lorem ipsum dolor sit amet, consectetur adipiscing elit, sed do eiusmod tempor incididunt ut labore et dolore magna aliqua. Ut enim ad min</p>
  <div class="contact-box">
    <div class="contact-info" role="img" aria-label="Happy couple with paint rollers, tinted navy">
      <div class="in">
        <h4>CONTACT US</h4>
        <div class="call">Call: 2095550183</div>
        <div class="mail">hello@brushharbor.example</div>
        <div class="blk"><b>Address:</b><br>SOME PLACE<br>51100 Road</div>
        <div class="blk"><b>Operating Hours</b><br>Monday to Saturday: 9:00 - 18:00<br>Sunday: Closed</div>
        <div class="socials"><span></span><span class="on"></span><span></span><span></span></div>
      </div>
    </div>
    <div class="form">
      <h4>FREE CONSULTATION</h4>
      <div class="field" style="top:110px">Your Name</div>
      <div class="field" style="top:160px">Email</div>
      <div class="field" style="top:208px">Phone</div>
      <div class="field" style="top:258px;height:92px">Message ...</div>
      <div class="btn">SUBMIT</div>
    </div>
  </div>
</section>

<footer class="section footer">
  <div class="infobar">
    <div class="info" style="left:38px">
      <svg width="54" height="46" viewBox="0 0 54 46" fill="none" stroke="#fff" stroke-width="1.6"><path d="M27 4a10 10 0 0 0-10 10c0 8 10 18 10 18s10-10 10-18A10 10 0 0 0 27 4z"/><circle cx="27" cy="14" r="4"/><path d="M14 28l-12 16h50l-12-16"/></svg>
      <div><h4>Address</h4><p>27 Canvas Row, Stockton, USA</p></div>
    </div>
    <div class="info" style="left:396px">
      <svg width="50" height="50" viewBox="0 0 24 24" fill="none" stroke="#fff" stroke-width="1"><path d="M5 2h4l2 5-3 2a11 11 0 0 0 7 7l2-3 5 2v4a2 2 0 0 1-2 2A19 19 0 0 1 3 4a2 2 0 0 1 2-2z"/></svg>
      <div><h4>Phone</h4><p>+1 209 555 0162</p></div>
    </div>
    <div class="info" style="left:754px">
      <svg width="48" height="48" viewBox="0 0 48 48" fill="none" stroke="#fff" stroke-width="1.6"><path d="M4 20l20-16 20 16v24H4z"/><path d="M4 20l20 14 20-14"/><rect x="12" y="10" width="24" height="18"/></svg>
      <div><h4>Email Contact</h4><p>hello@brushharbor.example</p></div>
    </div>
  </div>
  <div class="fcol" style="left:66px">
    <h4>About Us</h4><div class="rule"></div>
    <p>Lorem ipsum dolor sit amet, consectetur adipi elit, sed do eiusmod tempor incididunt ut lab dolore magna aliqua.</p>
    <a class="more">Read More</a>
  </div>
  <div class="fcol" style="left:433px">
    <h4>Useful Links</h4><div class="rule"></div>
    <div class="links"><a>About Us</a><a>Services</a><a>Projects</a><a>Shop</a><a>Blog</a><a>Privacy Policy</a><a>Contact Us</a><a>Help Desk</a></div>
  </div>
  <div class="fcol" style="left:796px">
    <h4>Useful Links</h4><div class="rule"></div>
    <p style="line-height:24px;width:330px">If you have any questions, Subscribe to our newsletter to get our latest products</p>
    <div class="sub" style="margin-top:12px"><div>Email</div><span><svg width="20" height="16" viewBox="0 0 20 16" fill="none" stroke="#fff" stroke-width="1.6"><path d="M1 8h17M11 1l7 7-7 7"/></svg></span></div>
  </div>
  <div class="fbottom">
    <div class="fbrand"><i></i>Brush Harbor</div>
    <div class="fsocial"><span><i></i></span><span><i></i></span><span><i></i></span><span><i></i></span></div>
  </div>
</footer>

</body>
</html>
```